Brivanta sales folder inserts

We need the same design for 4 separate service offerings to put inside our sales folder. Each insert should be laid out the same with different images and text and the 2nd, 3rd, and 4th should each be 3/4" shorter than the previous one so that when all 4 are inserted into the folder you see the black strip with text showing what the service offering is. Basically staggered inserts.

Industry/Entity Type

Information Technology

Font styles to use
Sans Serif

Colors
acd136

Requirements
Must have
• Brivanta logo and included text. Keep with the green Pantone 90 and black color scheme
Nice to have
• a better layout and pics

```html
<!DOCTYPE html>
<html lang="en">
<head>
<meta charset="utf-8">
<title>Brivanta sales folder inserts</title>
<link href="https://fonts.googleapis.com/css2?family=Roboto+Condensed:wght@400;500;700&display=swap" rel="stylesheet">
<style>
  :root {
    --brand-green: #acd136;
    --ink-black: #1c1c1c;
    --strip-dark: #2b2b2b;
    --strip-mid: #3d3d3d;
    --panel-dark: #353535;
    --panel-light: #e4e4e4;
    --text-white: #ffffff;
    --text-grey: #4a4a4a;
    --page-bg: #d9d9d9;
    --photo-deep: #1f3a55;
    --photo-light: #9fc3d6;
    --photo-warm: #c77a3a;
  }
  html, body {
    margin: 0;
    width: 1200px;
    height: 800px;
    overflow: hidden;
    background: var(--page-bg);
    font-family: "Roboto Condensed", Arial, sans-serif;
  }
  .insert-stack {
    position: relative;
    width: 1200px;
    height: 800px;
  }
  .insert {
    position: absolute;
    left: 300px;
    width: 600px;
    bottom: 50px;
    background: linear-gradient(180deg, var(--strip-mid) 0%, var(--strip-dark) 60%);
    box-shadow: 0 -2px 6px rgba(0,0,0,0.35);
  }
  .insert--business { top: 50px;  z-index: 1; }
  .insert--it       { top: 120px; z-index: 2; }
  .insert--secure   { top: 190px; z-index: 3; }
  .insert--voice    { top: 260px; z-index: 4; }

  .insert__headline {
    position: absolute;
    top: 12px;
    left: 20px;
    margin: 0;
    color: var(--text-white);
    font-size: 15px;
    font-weight: 500;
    letter-spacing: 0.06em;
    text-transform: uppercase;
    white-space: nowrap;
  }
  .insert--voice .insert__headline {
    font-size: 12px;
    font-weight: 400;
    top: 10px;
  }
  .service-tab {
    position: absolute;
    right: 0;
    width: 170px;
    height: 30px;
    background: var(--brand-green);
    clip-path: polygon(22px 0, 100% 0, 100% 100%, 0 100%);
    color: var(--text-white);
    font-size: 16px;
    font-weight: 500;
    letter-spacing: 0.04em;
    text-transform: uppercase;
    line-height: 30px;
    text-align: right;
    padding-right: 18px;
    box-sizing: border-box;
    white-space: nowrap;
  }
  .insert--business .service-tab,
  .insert--it .service-tab,
  .insert--secure .service-tab { top: 36px; }
  .insert--voice .service-tab { top: 14px; z-index: 2; }

  .hero-photo {
    position: absolute;
    top: 34px;
    left: 0;
    width: 100%;
    height: 200px;
    background:
      radial-gradient(circle at 22% 78%, var(--photo-warm) 0%, rgba(199,122,58,0) 28%),
      linear-gradient(100deg, var(--photo-deep) 0%, #3f6f8f 45%, var(--photo-light) 100%);
  }

  .brand-panel {
    position: absolute;
    top: 234px;
    left: 0;
    width: 260px;
    bottom: 0;
    background: var(--panel-light);
  }
  .brand-mark {
    position: absolute;
    top: 40px;
    left: 28px;
    display: flex;
    align-items: center;
    gap: 12px;
  }
  .brand-mark__square {
    width: 38px;
    height: 38px;
    background: var(--brand-green);
  }
  .brand-mark__name {
    color: var(--text-grey);
    font-size: 38px;
    font-weight: 500;
    letter-spacing: 0.04em;
    line-height: 1;
  }
  .brand-tagline {
    position: absolute;
    top: 96px;
    left: 28px;
    margin: 0;
    color: var(--brand-green);
    font-size: 13px;
    font-weight: 700;
    letter-spacing: 0.1em;
    text-transform: uppercase;
  }

  .service-panel {
    position: absolute;
    top: 234px;
    left: 260px;
    right: 0;
    bottom: 0;
    background: var(--panel-dark);
  }
  .device-photo {
    position: absolute;
    top: 28px;
    left: 70px;
    width: 220px;
    height: 140px;
    background: linear-gradient(135deg, #6f8fa8 0%, #c9d8e3 55%, #8aa3b6 100%);
    border: 6px solid var(--ink-black);
    border-radius: 6px 6px 0 0;
  }
  .assist-bar {
    position: absolute;
    left: 0;
    bottom: 34px;
    width: 250px;
    height: 32px;
    background: var(--brand-green);
    color: var(--ink-black);
    font-size: 15px;
    line-height: 32px;
    padding-left: 14px;
    box-sizing: border-box;
  }
</style>
</head>
<body>
<main class="insert-stack">

  <section class="insert insert--business">
    <h2 class="insert__headline">Bri-Business run anywhere, protect anything</h2>
    <div class="service-tab">Bri-Business</div>
  </section>

  <section class="insert insert--it">
    <h2 class="insert__headline">Bri-IT proactive IT support</h2>
    <div class="service-tab">Bri-IT</div>
  </section>

  <section class="insert insert--secure">
    <h2 class="insert__headline">Bri-Secure - secure your assets</h2>
    <div class="service-tab">Bri-Secure</div>
  </section>

  <section class="insert insert--voice">
    <h2 class="insert__headline">Bri-Voice - connect every call</h2>
    <div class="hero-photo" role="img" aria-label="Business person in a suit over a glowing city skyline with light trails"></div>
    <div class="service-tab">Bri-Voice</div>

    <div class="brand-panel">
      <div class="brand-mark">
        <span class="brand-mark__square"></span>
        <span class="brand-mark__name">BRIVANTA</span>
      </div>
      <p class="brand-tagline">Connecting every option</p>
    </div>

    <div class="service-panel">
      <div class="device-photo" role="img" aria-label="Laptop screen showing a hand drawing cloud and device network icons"></div>
      <div class="assist-bar">How can Brivanta assist?</div>
    </div>
  </section>

</main>
</body>
</html>
```